1 000,00 $ Garanti
LIMO BUS WEBSITE REDESIGN NEEDED
excited to see what you all come up with!!!
Transportation
www.zorvexride-example.com
We are a LUXURY LIMO BUS COMPANY that specialize in offering limo buses for rent. Unlike regular stretch limos our buses have more room, more lights, and give the customer an experience of a dance club on wheels. We target nights outs, weddings, proms, stags, birthdays.. All CDL chuaffered buses.
I don't like the flow of our existing website, and need to give us a better image with lots of excitement for the visitor yet we need to look professional.
Fun
SILVER - BLUE - BLACK
RED & BLACK
top
JUST BE CREATIVE AND COME UP WITH A EXCITING DESIGN THAT WILL WOW anyone and make them want to book with us. Our website must be able to open correctly on all browsers and cell phones. Our phone number must be clearly seen on all pages.
Here are THE PROFESSIONAL INTERIOR photos of the buses we have that you can use in the creative
another photo
more photos
BUS #1 CROPPED PHOTO
BUS #4 CROPPED PHOTO
PHOTO OF PIP TOPPER WAGON

```html
<!DOCTYPE html>
<html lang="en">
<head>
<meta charset="utf-8">
<title>Zorvex Transportation &amp; Tours</title>
<link rel="stylesheet" href="https://fonts.googleapis.com/css2?family=Arimo:wght@400;700&display=swap">
<style>
:root{
  --bg-deep:#020a18;
  --bg-glow:#0d3a78;
  --panel:#050608;
  --panel-edge:#2a3442;
  --silver:#d7dde6;
  --text:#c9ccd2;
  --muted:#8a9099;
  --blue:#3fa4ff;
  --blue-soft:#6cc0ff;
  --line:#39414d;
}
*{margin:0;padding:0;box-sizing:border-box}
html,body{width:1200px;height:895px;overflow:hidden}
body{
  background:radial-gradient(ellipse 560px 420px at 600px 420px,var(--bg-glow) 0%,#061a3c 45%,var(--bg-deep) 100%);
  font-family:"Arimo",Arial,sans-serif;color:var(--text);position:relative;
}
.site-frame{position:absolute;left:0;top:0;width:1200px;height:895px;
  filter:drop-shadow(0 0 26px rgba(63,164,255,.6)) drop-shadow(0 0 8px rgba(120,190,255,.5))}
.brand-bus{position:absolute;left:706px;top:96px;width:266px;height:84px;border-radius:30px 36px 8px 8px;
  background:linear-gradient(180deg,#8c95a3 0%,#3b4350 45%,#15191f 100%);border:2px solid #aab3bf}
.brand{position:absolute;left:440px;top:134px;width:270px;text-align:center;z-index:2}
.brand-name{font-size:58px;font-weight:700;color:var(--silver);letter-spacing:2px;line-height:1}
.brand-tag{font-size:14px;font-weight:700;color:var(--blue);margin-top:5px}
.contact-left{position:absolute;left:250px;top:194px;font-size:8px;line-height:11px;color:var(--muted);font-style:normal}
.contact-right{position:absolute;right:230px;top:192px;text-align:right;font-size:11px;line-height:13px;color:var(--silver)}
.contact-right strong{font-size:13px}
.contact-right small{font-size:8px;color:var(--muted)}
.nav{position:absolute;left:254px;top:244px;width:708px;display:flex;justify-content:space-between;
  font-size:15px;font-weight:700;color:#fff;text-shadow:0 0 8px var(--blue)}
.nav-rule{position:absolute;left:250px;top:270px;width:712px;height:1px;background:var(--line)}
.welcome{position:absolute;left:256px;top:296px;width:470px}
.welcome h1{font-size:13px;font-weight:400;color:#fff;margin-bottom:8px}
.welcome h1 span{color:var(--blue)}
.welcome p{font-size:8.6px;line-height:11px;margin-bottom:9px}
.video{position:absolute;left:752px;top:294px;width:201px;height:143px;border:1px solid #333;
  background:linear-gradient(135deg,#3a1f5e,#1d2a6b 50%,#0b0d1a)}
.video-bar{position:absolute;left:0;bottom:0;width:100%;height:16px;background:rgba(0,0,0,.7)}
.play{position:absolute;left:84px;top:52px}
.open-house{position:absolute;left:257px;top:472px;width:226px;padding:6px 8px;
  border:1px solid var(--blue);box-shadow:0 0 14px rgba(63,164,255,.7);
  font-size:12px;font-style:italic;line-height:14px;color:#fff}
.open-house b{color:var(--blue-soft);font-weight:400}
.specials{position:absolute;left:508px;top:464px;width:220px;font-size:8px;line-height:11px}
.section-title{font-size:12px;font-weight:700;color:var(--blue);margin-bottom:10px}
.specials p{margin-bottom:10px}
.featured{position:absolute;left:758px;top:464px;width:200px;font-size:8px;line-height:11px}
.thumbs{display:flex;gap:10px;margin-top:8px}
.thumbs div{width:42px;height:40px;background:linear-gradient(135deg,#2d6bb5,#4a2d7a);border:1px solid #555}
.gallery{position:absolute;left:250px;top:577px;width:712px;height:128px}
.arrow{position:absolute;top:44px}
.shot{position:absolute;top:0;height:126px;border:1px solid #444}
.shot-1{left:20px;width:116px;background:linear-gradient(135deg,#1a2a6e,#5b2f8a)}
.shot-2{left:148px;width:120px;background:linear-gradient(135deg,#5a2e7a,#1e3a8a)}
.shot-3{left:280px;width:114px;background:linear-gradient(135deg,#1b2450,#3b5cc0)}
.shot-4{left:406px;width:114px;background:linear-gradient(135deg,#2a4f9e,#7a4bb0)}
.shot-5{left:532px;width:160px;background:linear-gradient(180deg,#c8c6c0,#6d6a66)}
.socials{position:absolute;left:259px;top:712px;display:flex;gap:8px}
.socials span{width:22px;height:22px;background:#3b6fc4;border-radius:3px}
.footer-nav{position:absolute;left:380px;top:718px;display:flex;gap:14px;font-size:8px;color:var(--muted)}
.copyright{position:absolute;left:0;top:756px;width:1200px;text-align:center;font-size:8px;color:var(--muted)}
</style>
</head>
<body>
<svg class="site-frame" viewBox="0 0 1200 895" aria-hidden="true">
  <path d="M230,208 Q230,184 254,184 L416,184 Q436,184 446,160 Q458,132 488,132 L956,132 Q982,132 982,158 L982,727 Q982,751 958,751 L254,751 Q230,751 230,727 Z" fill="var(--panel)" stroke="var(--panel-edge)" stroke-width="2"/>
</svg>
<div class="brand-bus" role="img" aria-label="Photo of a white luxury limousine bus"></div>
<div class="brand">
  <div class="brand-name">ZORVEX</div>
  <div class="brand-tag">Transportation &amp; Tours, LLC</div>
</div>

<address class="contact-left">Zorvex Transportation and Tours, LLC<br><br>42 Harlow Ave Suite 3<br>Eastbrook, NY 10000</address>
<div class="contact-right"><strong>(555) 014-2200</strong> - Office<br><strong>(555) 019-3370</strong> - Toll Free<br><small>Please call for reservations and pricing</small></div>

<nav class="nav"><span>Home</span><span>Limo Bus Photos</span><span>Celebrity Customer Photos</span><span>Packages</span><span>Corporate</span><span>About Us</span><span>Links</span><span>Contact Us</span></nav>
<div class="nav-rule"></div>

<section class="welcome">
  <h1>Welcome to <span>ZORVEX</span> website</h1>
  <p>At Zorvex Transportation &amp; Tours, LLC, we are proud of our reputation for outstanding customer service with one of the newest and most impressive fleets in Western New York. We are recognized as the premier limousine bus company in the region - a reputation which has grown significantly since the company began several years ago.</p>
  <p>We now offer limousine buses along with a reputation for customer service which is unmatched in the region. We hire only professional licensed drivers who treat every guest with the highest level of care. From weddings, proms, wine tours, sports and concerts, we are providing VIP transportation, all of us at Zorvex recognize the importance of each and every booking. We provide our customers with only the best in service and transportation. Thank you to our thousands of satisfied customers from around the country and Canada.</p>
</section>

<div class="video" role="img" aria-label="Video of a limo bus interior with party lights">
  <svg class="play" width="34" height="34" viewBox="0 0 34 34"><circle cx="17" cy="17" r="16" fill="rgba(0,0,0,.55)"/><path d="M13 10 L24 17 L13 24 Z" fill="#fff"/></svg>
  <div class="video-bar"></div>
</div>

<div class="open-house">Every Wednesday Night from 5 pm to 8 pm <b>OPEN HOUSE</b>. Come check out our <b>LUXURY</b> buses in person and see why we have the best fleet in Western New York.</div>

<section class="specials">
  <div class="section-title">Managers Specials</div>
  <p>Call About Wine Tour &amp; Night Out Specials</p>
  <p>PROM NIGHT IS APPROACHING SOON,<br>MAKE SURE TO BOOK YOUR LIMO.</p>
  <p>$60 PER STUDENT, 5 HOUR SPLIT</p>
</section>

<section class="featured">
  <div class="section-title">Featured</div>
  <p>Western New York's Newest and Most<br>Luxurious Limousine Buses</p>
  <div class="thumbs"><div role="img" aria-label="Limo bus exterior thumbnail"></div><div role="img" aria-label="Limo bus interior thumbnail"></div></div>
</section>

<div class="gallery">
  <svg class="arrow" style="left:0" width="14" height="36" viewBox="0 0 14 36"><path d="M12 2 L2 18 L12 34" fill="none" stroke="var(--blue)" stroke-width="3"/></svg>
  <div class="shot shot-1" role="img" aria-label="Limo bus interior with blue lighting"></div>
  <div class="shot shot-2" role="img" aria-label="Limo bus interior with purple lighting"></div>
  <div class="shot shot-3" role="img" aria-label="Limo bus lounge seating"></div>
  <div class="shot shot-4" role="img" aria-label="Limo bus dance floor lights"></div>
  <div class="shot shot-5" role="img" aria-label="Pip Topper Wagon vintage limousine"></div>
  <svg class="arrow" style="left:698px" width="14" height="36" viewBox="0 0 14 36"><path d="M2 2 L12 18 L2 34" fill="none" stroke="var(--blue)" stroke-width="3"/></svg>
</div>

<div class="socials"><span></span><span></span></div>
<nav class="footer-nav"><span>Home</span><span>Limo Bus Photos</span><span>Celebrity Customer Photos</span><span>Packages</span><span>Corporate</span><span>About Us</span><span>Links</span><span>Contact Us</span></nav>

<div class="copyright">&copy; Zorvex Transportation &amp; Tours LLC 2011</div>
</body>
</html>
```